Meridian Growth Works (MGW)

Create a Flyer similar to the example or better

Target Market(s)

Management of Corporate Companies

Requirements
Must have
• follow the PDF-example
Nice to have
• compelling

```html
<!DOCTYPE html>
<html lang="en">
<head>
<meta charset="utf-8">
<title>Meridian Growth Works – Retreat Flyer</title>
<link href="https://fonts.googleapis.com/css2?family=Lato:wght@400;700;900&family=Raleway:wght@700;800&display=swap" rel="stylesheet">
<style>
  :root {
    --navy: #1d2254;
    --gold: #c8a84a;
    --ink: #1f1f2a;
    --sea-deep: #0f5d7a;
    --sea-light: #4fa3b8;
    --mist: #eef0f1;
    --mist-dark: #c9cdd0;
    --photo-warm: #b9a585;
    --photo-cool: #8a96a3;
  }
  * { margin: 0; padding: 0; box-sizing: border-box; }
  html, body { width: 1200px; height: 848px; overflow: hidden; background: #fff; }
  .flyer {
    position: relative; width: 1200px; height: 848px; overflow: hidden;
    font-family: "Lato", Arial, sans-serif; color: var(--ink);
  }
  .backdrop {
    position: absolute; inset: 0;
    background:
      radial-gradient(ellipse at 55% 30%, #ffffff 0%, var(--mist) 40%, var(--mist-dark) 100%);
  }
  .waves { position: absolute; left: 0; top: 0; width: 1200px; height: 848px; }

  .column { position: absolute; font-size: 9.4px; line-height: 1.42; }
  .column p { margin-bottom: 8px; }
  .col-left { left: 46px; top: 64px; width: 196px; }
  .col-mid { left: 410px; top: 64px; width: 300px; }
  .col-right { left: 918px; top: 64px; width: 246px; }

  .section-title {
    font-family: "Lato", Arial, sans-serif; font-weight: 900;
    color: var(--navy); text-transform: uppercase;
    font-size: 13px; line-height: 1.2; margin: 8px 0 8px;
  }
  .day-title, .side-title {
    font-family: "Raleway", Arial, sans-serif; font-weight: 800;
    color: var(--navy); font-size: 13px; line-height: 1.3; margin: 6px 0 5px;
  }
  .col-mid p, .col-mid .step { font-size: 9.4px; }
  .step { padding-left: 24px; margin: 2px 0 6px; }
  .justify { text-align: justify; }

  .photo {
    position: absolute; width: 132px; height: 100px;
    border: 1px solid #d8d8d8;
  }
  .photo.warm { background: linear-gradient(160deg, #d9cbb2, var(--photo-warm)); }
  .photo.cool { background: linear-gradient(160deg, #aab3bd, var(--photo-cool)); }
  .photo.team { background: linear-gradient(170deg, #6e6a66, #3e4450); }
  .photo.sky { background: linear-gradient(180deg, #9fc3e6 0%, #dfe8ee 45%, #c7b596 100%); }
  .photo.pool { background: linear-gradient(180deg, #b9d1e8 0%, #e9ebe6 50%, #6fc3d6 100%); }
</style>
</head>
<body>
<div class="flyer">
  <div class="backdrop" role="img" aria-label="Faded photograph of a breaking ocean wave with a surfer"></div>

  <svg class="waves" viewBox="0 0 1200 848" aria-hidden="false">
    <defs>
      <linearGradient id="sea" x1="0" y1="0" x2="0" y2="1">
        <stop offset="0" stop-color="#3d8ea6"/>
        <stop offset="1" stop-color="#0c4f6a"/>
      </linearGradient>
    </defs>
    <path role="img" aria-label="Photograph of deep blue ocean water with white foam"
          d="M0 772 Q260 812 600 798 Q900 780 1200 700 L1200 848 L0 848 Z" fill="url(#sea)"/>
    <path d="M0 704 Q170 716 320 764 Q470 810 680 772 Q900 730 1200 706 L1200 720 Q920 742 690 790 Q470 832 310 786 Q160 742 0 736 Z" fill="var(--gold)"/>
    <path d="M360 770 Q560 708 840 692 Q1020 684 1200 684 L1200 704 Q960 712 720 768 Q560 806 420 786 Q385 780 360 770 Z" fill="var(--navy)"/>
  </svg>

  <section class="column col-left">
    <h2 class="section-title">Our local infrastructure for this retreat (the Masseria)</h2>
    <p>The Masseria (and Italian off-side estate) offers space for up to 10 innovators within the lovely and healthy environment of Apulia representing a totally refurbished, climatized and perfectly maintained first-class hospitality. The area also offers sufficient space for distraction and collection of thoughts, ideas and profound innovations. The intermediate MGW process steps will situationally be conducted either inside the climatized meeting rooms or on the covered country yard – or even in the form of focused off-side interventions in the open nature. The...</p>
    <h2 class="section-title">How you can tailor your individual MGW process</h2>
    <p>During the preparation of this retreat we are able to tailor the complete process to your specific needs and individualized requirements. All accommodation and dining (breakfast, lunch and dinner buffet) for the time of your innovator's stay with us is covered and ensured. Your innovators will be fully covered by a specific event-insurance.</p>
    <h2 class="section-title">The investment</h2>
    <p>As the complete process, content wise, can and will be tailored to your specific needs and expectations there is no unique price tag attached to it. Nevertheless, here is an indication of a cost tag for the MGW process (based on Theory U): € 12.000 – € 15.000 (excl. VAT) per person / 5-days. This indication has to be understood as the price including all services from the Departure Airport Brindisi-International and back.</p>
  </section>

  <div class="photo cool" style="left:256px;top:68px" role="img" aria-label="Photo of a workshop room with participants at flipcharts"></div>
  <div class="photo team" style="left:256px;top:236px" role="img" aria-label="Photo of a cheering team group"></div>
  <div class="photo cool" style="left:256px;top:402px" role="img" aria-label="Photo of a meeting room with a circle of chairs"></div>
  <div class="photo cool" style="left:256px;top:568px" role="img" aria-label="Photo of a whiteboard wall in a meeting room"></div>

  <section class="column col-mid">
    <h3 class="day-title">Day 1: Downloading pattern from the past (9 hours)</h3>
    <p>The focus of our work today, is your current situation in the context, which we defined for this particular 5 day MGW process.</p>
    <p class="step">Suspending</p>
    <p>Finding and applying options and opportunities to overcome your company's traditional thinking and collaboration attitude.</p>
    <p class="step">Re-Directing</p>
    <p class="step">Letting Go</p>
    <h3 class="day-title">Day 2: Presencing and identification of the organization's blind spots (12 hours)</h3>
    <p>The focus of our work today are questions and tasks around the purpose and sense of your current processes, attitudes and the organization's contributors. Identifying the blind spots by answering questions such as "Who is myself in the process?" and "What is my work and responsibility – on the whole".</p>
    <h3 class="day-title">Day 3: Letting the options come and crystallization of valuable solutions (12 hours)</h3>
    <p>Text to follow</p>
    <h3 class="day-title">Day 4: Crystallization, concretization &amp; prototyping – How might we.. (12 hours)</h3>
    <p>Text to follow</p>
    <h3 class="day-title">Day 5: Developing prototypes for processes and innovations &amp; Initiation of performing (How to get the job done...) (8 hours)</h3>
    <p>Text to follow</p>
    <p class="justify" style="margin-top:14px">Around 16:30 the shuttle service will be waiting to transport the innovators back to Brindisi-International-Airport. Our staff will guide your innovators back to the Airport the journey stared. From here your organization will have the chance and challenge to reflect, to adopt and to implement the working results of your innovators.</p>
    <p class="justify" style="margin-top:12px">The MGW process conducted during this retreat covers in total more than 50 hours of intense refection, extraction and intervention time – so the results will be profound and, once implemented, your business will be enabled toward the next level of efficiency and performance.</p>
  </section>

  <div class="photo sky" style="left:775px;top:68px" role="img" aria-label="Photo of a stone gate under olive trees"></div>
  <div class="photo sky" style="left:775px;top:236px" role="img" aria-label="Photo of a restored stone farmhouse with lawn"></div>
  <div class="photo pool" style="left:775px;top:402px" role="img" aria-label="Photo of a whitewashed trullo beside a pool"></div>
  <div class="photo pool" style="left:775px;top:568px" role="img" aria-label="Photo of a pool and shaded terrace"></div>

  <section class="column col-right">
    <h3 class="side-title">Set-up, preparation and execution...</h3>
    <p>Our Meridian Growth Works (MGW) process follows the principals of the Theory U (C) approach and is based on application of Agile principals and methodologies of Design Thinking and SCRUM. The aim of the MGW process is to enable your corporate organization to anticipate the requirements of the era of "Disruptive Innovation". (1.) Our joint journey starts with the assessment of your organization's best brains – jointly we prepare your specific content and process targets – and we will integrate them into our given structure. (2.) We enable your eligible contributors with tools and methodologies – to succeed successfully with the process. (3.) During the process with facilitation at our estate in Italy, your organization's contributors will apply their technical and business competence in accordance with the principals of the MGW process. (4.) In teams, (amount to be defined) your organization's contributors are guided through the Theory "U" process – and the innovation and creation of innovative and feasible business concepts are almost guaranteed. (5) After the completion of the MGW process, your facilitators (if you wish), with Harborline Advisory &amp; Coaching LLC support, will ensure the implementation of the elaborated innovation in the context of your corporate organization. Important: Our aim is to enable your organization to innovate on demand – we support you in the execution and the preparation of related steps on demand – and at your request.</p>
    <h3 class="side-title" style="margin-top:10px">How the MGW process will be conducted...</h3>
    <p>Together with your chosen management staff (your innovators) you will retreat to our pre-configured facility in Italy. We shall pick up the innovators at the import of your choice and fly with them to the international airport of Brindisi (I). From Brindisi-Airport we will guide and accompany the innovators via our shuttle service to our first-class maintained Masseria (the retreat). We will arrive there at around 10.00 a.m. After a brief welcome our process will start at around 11.00 a.m. with the first step of the U-Process:</p>
  </section>
</div>
</body>
</html>
```